BRVL Brochure Design

Northfield Council of Clinical Standards (BRVL) needs a whole new brochure. I've upload EPS logos and past brochures. Our tagline is to "modernize healthcare" and we think our brochure should reflect that, so that's the purpose of this project.

BRVL is a proven leader in healthcare education, training and
consulting services for health professionals. We’ve earned a reputation for excellence in healthcare quality improvement and management.

BRVL works to improve healthcare quality by educating healthcare professionals about healthcare best practices. We focus on instructing our clients on how to plan for, measure, and improve healthcare quality in all facilities and facets such as:

Patient Safety
Infection Control
Performance Improvement
Risk Management
Compliance and Accreditation
Health and Hospital Administration
Health Insurance
Healthcare Financial Management
Facility Management and Safety

DESIGN SUGGESTIONS:

Brochure Size: 8.5 X 11 full size brochure or 8.5 X 11 trifold brochure

Number of Pages: 2 to 3

Colors: Feel free to use a wide array of colors but try to stay away from colors that are too loud, ex: Pink, Purple, Neon Green.

Themes: Professional, Educational

Designs:

Pelor by Oskar Lindqvist

Quorvo Pamphlet by Derek Malloway

Lanterns for harvest by Solvendri

Paisaje de Sr KT by vrpl

http://www.plimbask.com/post/28461937205/10-creative-brochure-designs

Don't limit yourself to these examples. However, these are examples we liked

Reason: We would like to see more designs

We want more full page designs than tri-fold 

We are considering both tri-fold and full-page but would like to see more full page designs 

Reason: Our lead designer making the decisions on this project has been fired. I apologize for the inconvenience. We want extend the project one last time

Target Market(s)

Students, Doctors, and Educational Professionals

Industry/Entity Type

Healthcare

Logo Text

asdfasdf

Font styles to use
Serif
Sans Serif
Decorative
Script

Requirements
Should not have
• Pink, Purple, Neon Green colors

```html
<!DOCTYPE html>
<html lang="en">
<head>
<meta charset="utf-8">
<title>BRVL Brochure</title>
<link href="https://fonts.googleapis.com/css2?family=Bebas+Neue&family=PT+Sans+Narrow:wght@400;700&family=Open+Sans:wght@400;600&display=swap" rel="stylesheet">
<style>
  :root {
    --stage: #2a2a2c;
    --paper: #ffffff;
    --blue: #1a87cf;
    --blue-light: #2596dc;
    --navy: #0d3a7a;
    --band-grey: #7d7f82;
    --text-grey: #6b6d70;
    --dark-grey: #555759;
    --headline-blue: #1c82c8;
    --white: #ffffff;
  }
  * { box-sizing: border-box; margin: 0; padding: 0; }
  html, body { width: 1200px; height: 793px; overflow: hidden; }
  body { background: var(--stage); position: relative; font-family: "PT Sans Narrow", sans-serif; }

  .brochure {
    position: absolute; left: 90px; top: 90px;
    width: 1020px; height: 613px;
    background: var(--paper);
    overflow: hidden;
  }

  /* Photo spread */
  .hero-photo {
    position: absolute; left: 0; top: 0; width: 760px; height: 392px;
    background: linear-gradient(100deg, #e9e4de 0%, #cfc3b6 22%, #8a6a55 40%, #b9aea6 55%, #5b4c44 66%, #3b2f2b 100%);
  }
  .course-shade {
    position: absolute; left: 470px; top: 0; width: 290px; height: 392px;
    background: linear-gradient(90deg, rgba(40,30,28,0.25), rgba(30,22,20,0.55));
  }
  .courses {
    position: absolute; left: 490px; top: 20px; width: 262px; color: var(--white);
  }
  .courses h2 {
    font-family: "Bebas Neue", sans-serif; font-weight: 400;
    font-size: 40px; line-height: 36px; letter-spacing: 0.5px; margin-bottom: 8px;
  }
  .courses ul { list-style: none; }
  .courses li { font-size: 12px; line-height: 18.5px; white-space: nowrap; }

  .brand {
    position: absolute; left: 36px; top: 358px; display: flex; align-items: center; gap: 6px;
    font-family: "PT Sans Narrow", sans-serif; font-weight: 700; font-size: 21px; color: var(--navy);
  }
  .brand-dot { width: 18px; height: 18px; border-radius: 50%; background: var(--navy); }

  /* Membership */
  .membership-band {
    position: absolute; left: 0; top: 392px; width: 760px; height: 34px;
    background: var(--band-grey); display: flex; align-items: center; padding-left: 36px; gap: 38px;
  }
  .membership-band h2 {
    font-family: "Bebas Neue", sans-serif; font-weight: 400; font-size: 30px; color: var(--white); letter-spacing: 0.5px; padding-top: 3px;
  }
  .membership-band p { font-size: 12.5px; color: var(--white); }

  .plans { position: absolute; left: 36px; top: 440px; width: 700px; display: flex; gap: 26px; }
  .plan { width: 216px; color: var(--text-grey); position: relative; height: 140px; }
  .plan h3 {
    font-family: "Bebas Neue", sans-serif; font-weight: 400; font-size: 22px; color: var(--headline-blue); letter-spacing: 0.3px; line-height: 22px;
  }
  .plan p { font-size: 12.5px; line-height: 14.5px; text-align: justify; }
  .dues {
    position: absolute; left: 0; right: 0; bottom: 0; display: flex; justify-content: space-between;
    font-size: 12.5px; font-weight: 700; color: var(--dark-grey);
  }

  .base-strip { position: absolute; left: 0; bottom: 0; width: 760px; height: 16px; background: var(--navy); }

  /* Workshops panel */
  .workshops {
    position: absolute; left: 760px; top: 0; width: 260px; height: 613px;
    background: linear-gradient(180deg, var(--blue) 0%, var(--blue-light) 100%);
    color: var(--white); padding: 20px 18px 0 16px;
  }
  .workshops h2 {
    font-family: "Bebas Neue", sans-serif; font-weight: 400; line-height: 0.9;
  }
  .workshops h2 .big { display: block; font-size: 54px; }
  .workshops h2 .small { display: block; font-size: 33px; }
  .intro { font-size: 9.5px; line-height: 12.6px; margin-top: 12px; text-align: justify; }
  .lead { font-family: "Open Sans", sans-serif; font-size: 11px; line-height: 13.5px; margin-top: 14px; }
  .topics { list-style: none; margin-top: 10px; padding-left: 4px; }
  .topics li { font-family: "Open Sans", sans-serif; font-size: 11px; line-height: 19.5px; }
</style>
</head>
<body>
  <article class="brochure">
    <div class="hero-photo" role="img" aria-label="Photograph of a smiling healthcare professional in a striped shirt, a colleague blurred behind her"></div>
    <div class="course-shade"></div>

    <section class="courses">
      <h2>Future Course<br>Offerings</h2>
      <ul>
        <li>Fellowship in Medical/Healthcare Quality</li>
        <li>Fellowship in Hospital Management</li>
        <li>Certified in Facility Management and Safety (CFMS)</li>
        <li>Certificate in Medication Safety (CMS)</li>
        <li>Certificate in Healthcare Insurance and Finance (CHIF)</li>
        <li>Certification in Healthcare Human Resources Management</li>
        <li>Certification in Waste Management for Healthcare</li>
        <li>Certification in Revenue Cycle Management</li>
        <li>Certification in Lean/Six Sigma—Green Belt</li>
        <li>Certification in Lean/Six Sigma—Black Belt</li>
        <li>Certification in Business Process Management</li>
        <li>Graduate Diploma in Healthcare Quality (DHQ)</li>
        <li>Graduate Diploma in Infection Control (DIC)</li>
        <li>Graduate Diploma in Nursing Management (DNM)</li>
        <li>Online Education and Exam Capabilities</li>
      </ul>
    </section>

    <div class="brand"><span class="brand-dot"></span>BRVL</div>

    <div class="membership-band">
      <h2>Membership Products</h2>
      <p>BRVL offers several kinds of membership to meet your varied needs.</p>
    </div>

    <section class="plans">
      <div class="plan">
        <h3>Personal Membership</h3>
        <p>If you want to become an BRVL member for your own personal and professional development, consider a personal membership.</p>
        <div class="dues"><span>Annual</span><span>Dues:</span><span>$100</span></div>
      </div>
      <div class="plan">
        <h3>Group Membership</h3>
        <p>If you would like to procure membership for multiple people in your institution, consider a group membership, which offers: membership for up to 15 people up to 3 subscriptions to the JBRVL, Journal of the Northfield Council of Clinical Standards</p>
        <div class="dues"><span>Annual</span><span>Dues:</span><span>$350</span></div>
      </div>
      <div class="plan">
        <h3>Student Membership</h3>
        <p>If you are a student studying a health related field or have an interest in improving the quality of care available to the public, consider a student membership, which gives: all the benefits of regular membership special student rates to the BRVL conference</p>
        <div class="dues"><span>Annual</span><span>Dues:</span><span>$25</span></div>
      </div>
    </section>

    <div class="base-strip"></div>

    <aside class="workshops">
      <h2><span class="big">Workshops</span><span class="small">and Seminars</span></h2>
      <p class="intro">The Northfield Council of Clinical Standards is proud to offer products that recognize the dedication of those who invest in their education and professional development. We are the only organization focused on quality in healthcare to offer regular training in seven different fields of healthcare quality. All of our certificate courses target areas that contribute to creating an overall safer and higher quality healthcare environment, and each specialized course focuses on delivering actionable knowledge so that you get the tools you need to make a positive impact on healthcare outcomes. The Council also offers a fellowship program that highlights the spectacular achievements of those who have made deep commitments to improving quality and patient safety in healthcare.</p>
      <p class="lead">BRVL training workshops address a variety of topics important to the success of your healthcare organization such as:</p>
      <ul class="topics">
        <li>Teambuilding</li>
        <li>Leadership</li>
        <li>Quality assurance</li>
        <li>Quality improvement</li>
        <li>Accreditation</li>
        <li>Performance measurement</li>
        <li>Customer service</li>
        <li>Standards and communication</li>
        <li>Strategic planning</li>
        <li>Applied research</li>
        <li>Survey design / methodology</li>
        <li>Re-engineering</li>
        <li>The Six Sigma method.</li>
      </ul>
    </aside>
  </article>
</body>
</html>
```